K Brode Artist Business Card

I need a business card for myself working as an emerging artist. I have an artwork that has been exhibited at an Awards exhibition that I would like incorporated into my business card. The card needs to be simple but different so I was thinking about one that is perhaps half or 1/3 of the normal business card size so that it could be slipped comfortably into little pouches. I only want my name, email, mobile number and facebook artist page link on the card.Perhaps the artwork on the size of a normal business card and then the card chopped up into 3 so that I have 3 business cards of different look and my details on the blank side of the card..unless someone can come up with a more interesting concept that is simple and fit for an emerging artist :)

```html
<!DOCTYPE html>
<html lang="en">
<head>
<meta charset="UTF-8">
<title>K Brode Artist Business Card</title>
<link rel="stylesheet" href="https://fonts.googleapis.com/css2?family=Kaushan+Script&family=Questrial&display=swap">
<style>
  :root {
    --page-bg: #ece8e3;
    --card-bg: #ffffff;
    --name-red: #e8402c;
    --text-grey: #4a4a4a;
    --icon-lime: #c9c41c;
    --icon-red: #e8452f;
    --icon-maroon: #8e1b1e;
    --art-red: #d9381e;
    --art-orange: #ee8a2a;
    --art-yellow: #eed36a;
    --art-green: #8fae3c;
  }
  * { margin: 0; padding: 0; box-sizing: border-box; }
  html, body { width: 1200px; height: 1000px; overflow: hidden; }
  body {
    background: var(--page-bg);
    display: flex;
    align-items: center;
    justify-content: center;
    gap: 60px;
  }
  .card {
    width: 480px;
    height: 480px;
    border-radius: 34px;
    overflow: hidden;
    box-shadow: 0 6px 18px rgba(0,0,0,0.12);
  }
  .card-artwork {
    background:
      radial-gradient(ellipse at 45% 35%, var(--art-red) 0%, var(--art-orange) 40%, transparent 70%),
      linear-gradient(180deg, var(--art-yellow) 0%, var(--art-yellow) 60%, var(--art-green) 100%);
  }
  .card-details {
    background: var(--card-bg);
    display: flex;
    flex-direction: column;
    align-items: center;
    padding-top: 150px;
    font-family: "Questrial", sans-serif;
    color: var(--text-grey);
    text-align: center;
  }
  .artist-name {
    font-family: "Kaushan Script", cursive;
    color: var(--name-red);
    font-size: 58px;
    font-weight: 400;
    line-height: 1;
    margin-bottom: 28px;
  }
  .contact-icon { width: 24px; height: 24px; display: block; }
  .contact-line {
    font-size: 22px;
    line-height: 1.2;
    margin: 4px 0 8px;
  }
</style>
</head>
<body>
  <div class="card card-artwork" role="img" aria-label="Painting of a tree with red and orange autumn foliage above a green and yellow meadow"></div>

  <div class="card card-details">
    <h1 class="artist-name">K Brode</h1>

    <svg class="contact-icon" viewBox="0 0 24 24" aria-hidden="true">
      <circle cx="12" cy="12" r="11" fill="var(--icon-lime)"/>
      <circle cx="12" cy="12" r="9.5" fill="none" stroke="#fff" stroke-width="1"/>
      <rect x="8.5" y="5.5" width="7" height="13" rx="1.2" fill="#fff"/>
      <rect x="9.7" y="7" width="4.6" height="4" fill="var(--icon-lime)"/>
      <g fill="var(--icon-lime)">
        <rect x="9.7" y="12.3" width="1.2" height="1.2"/><rect x="11.4" y="12.3" width="1.2" height="1.2"/><rect x="13.1" y="12.3" width="1.2" height="1.2"/>
        <rect x="9.7" y="14.2" width="1.2" height="1.2"/><rect x="11.4" y="14.2" width="1.2" height="1.2"/><rect x="13.1" y="14.2" width="1.2" height="1.2"/>
      </g>
    </svg>
    <p class="contact-line contact-phone">021 555014</p>

    <svg class="contact-icon" viewBox="0 0 24 24" aria-hidden="true">
      <circle cx="12" cy="12" r="11" fill="var(--icon-red)"/>
      <circle cx="12" cy="12" r="9.5" fill="none" stroke="#fff" stroke-width="1"/>
      <rect x="6.5" y="8" width="11" height="8" fill="#fff"/>
      <path d="M6.5 8 L12 12.5 L17.5 8" fill="none" stroke="var(--icon-red)" stroke-width="1"/>
    </svg>
    <p class="contact-line contact-email">hello@kbrodeart.com</p>

    <svg class="contact-icon" viewBox="0 0 24 24" aria-hidden="true">
      <circle cx="12" cy="12" r="11" fill="var(--icon-maroon)"/>
    </svg>
    <p class="contact-line contact-social">social.example/pages/Kbrodeartist</p>
  </div>
</body>
</html>
```